business card deign

Logo needs the following on it.
1. attached logo
2. Tagline - "From chilled coolers to party gear...we bring it all along!"
3. Name- Delia Fenwick, Founder and CPO
4. Address - 418 E. Harlow Avenue, Ste 2204, Tampa, FL. 33719
5. Phone - 720.555.0187

```html
<!DOCTYPE html>
<html lang="en">
<head>
<meta charset="utf-8">
<title>Kelvera Business Card</title>
<link rel="stylesheet" href="https://fonts.googleapis.com/css2?family=Poppins:wght@400;600&family=Raleway:wght@300&display=swap">
<style>
  :root {
    --backdrop: #8a8a8b;
    --ink: #060608;
    --paper: #ffffff;
    --band-grey: #8e8e91;
    --back-card: #151515;
    --back-text: #d4d4d4;
  }
  html, body {
    margin: 0;
    padding: 0;
    width: 1188px;
    height: 1200px;
    overflow: hidden;
    background: var(--backdrop);
  }
  .canvas {
    position: relative;
    width: 1188px;
    height: 1200px;
  }
  .card {
    position: absolute;
    left: 245px;
    width: 696px;
    height: 386px;
    overflow: hidden;
  }
  .card--front { top: 159px; background: var(--paper); }
  .card--back { top: 627px; background: var(--back-card); }
  .wave { position: absolute; inset: 0; width: 100%; height: 100%; }
  .contact {
    position: absolute;
    left: 63px;
    top: 143px;
    color: var(--paper);
    font-family: "Poppins", sans-serif;
  }
  .contact__name { margin: 0; font-size: 25px; font-weight: 600; line-height: 1.1; }
  .contact__title { margin: 2px 0 0; font-size: 18px; font-weight: 400; line-height: 1.3; }
  .contact__address { margin: 16px 0 0; font-size: 18px; line-height: 1.35; }
  .contact__list { list-style: none; margin: 14px 0 0; padding: 0; font-size: 18px; line-height: 1.45; }
  .contact__list li { display: flex; align-items: center; gap: 9px; }
  .contact__icon { width: 20px; height: 16px; fill: var(--paper); }
  .brand-name {
    position: absolute;
    font-family: "Poppins", sans-serif;
    font-weight: 600;
    letter-spacing: 0.32em;
    margin: 0;
  }
  .card--front .brand-name {
    left: 428px;
    top: 170px;
    font-size: 30px;
    color: var(--ink);
  }
  .card--back .brand-name {
    left: 0;
    right: 0;
    top: 238px;
    text-align: center;
    font-size: 34px;
    color: var(--back-text);
    padding-left: 0.32em;
  }
  .tagline {
    position: absolute;
    left: 0;
    right: 0;
    top: 319px;
    margin: 0;
    text-align: center;
    font-family: "Raleway", sans-serif;
    font-weight: 300;
    font-size: 17px;
    color: var(--back-text);
  }
</style>
</head>
<body>
<main class="canvas">
  <section class="card card--front">
    <svg class="wave" viewBox="0 0 696 386" preserveAspectRatio="none" aria-hidden="true">
      <path d="M71 52 C190 58 270 140 376 232 C450 296 540 300 696 236 L696 270 C560 330 440 310 376 245 Z" fill="var(--band-grey)"/>
      <path d="M0 62 C150 40 250 130 376 245 C450 312 560 330 696 270 L696 386 L0 386 Z" fill="var(--ink)"/>
    </svg>
    <div class="contact">
      <h1 class="contact__name">Delia Fenwick</h1>
      <p class="contact__title">Founder and CPO</p>
      <p class="contact__address">418 E. Harlow Avenue,<br>Ste 2204, Tampa, FL. 33719</p>
      <ul class="contact__list">
        <li>
          <svg class="contact__icon" viewBox="0 0 20 16" aria-hidden="true"><path d="M1 5 C1 1 19 1 19 5 L15 6 L14 4 C12 3.4 8 3.4 6 4 L5 6 Z M5 8 L15 8 L17 15 L3 15 Z"/><circle cx="10" cy="11" r="2.2" fill="var(--ink)"/></svg>
          <span>720.555.0187</span>
        </li>
        <li>
          <svg class="contact__icon" viewBox="0 0 20 16" aria-hidden="true"><path d="M1 3 L19 3 L19 4 L10 9 L1 4 Z M1 6 L10 11 L19 6 L19 14 L1 14 Z"/></svg>
          <span>info@deliafenwick.com</span>
        </li>
      </ul>
    </div>
    <p class="brand-name">KELVERA</p>
  </section>

  <section class="card card--back">
    <p class="brand-name">KELVERA</p>
    <p class="tagline">From chilled coolers to party gear...we bring it all along!</p>
  </section>
</main>
</body>
</html>
```